Brochure Design Project

Need a new look. Customer wants to update 10 year old literature. Very similar "text content" and color scheme only. Need a new modern look. Clean fonts...maybe distressed fonts. Nice salon. Would like brochure to be consistent with their decor...possibly "curvey" graphics maybe simple die-cut if cost effective to produce. Use your imagination! Showed them some pixel harbor work that they liked the look of and I will share these details so you have a feel for the type of work we are looking for.
Updates

Reason: My customer has reviewed the art submissions and though she likes the ideas presented, she has indicated that she needs to stay more consistent with some other collateral which means she would prefer a more mono-chromatic (maybe two or three colors but not a full color glossy brochure. Keeping in mind that she would like a matte look please offer design selections. She has sent me some images of the other collateral she would possibly like to coordinate with which I can send via email upon request.

Target Market(s)

Salon Patrons

Industry/Entity Type

Salon

Requirements
Must have
• Packaged InDesign file upon completion so we can edit down the line(update prices etc.) High Res PDF with marks and bleeds. Must fit into No. 10 envelope(4.125" x 9.5") once folded...I am thinking 9x16 but am open to ideas.
Should not have
• photos...or limit

```html
<!DOCTYPE html>
<html lang="en">
<head>
<meta charset="utf-8">
<title>Salon Services Brochure</title>
<link href="https://fonts.googleapis.com/css2?family=Asap+Condensed:wght@400;500;600&display=swap" rel="stylesheet">
<style>
  :root {
    --page: #ffffff;
    --olive-panel: #c5c092;
    --green-text: #6e9214;
    --tan-head: #b7b27c;
    --white: #ffffff;
    --fold: #555555;
    --photo-warm: #e9cbb5;
    --photo-soft: #f1e4da;
  }
  * { box-sizing: border-box; margin: 0; padding: 0; }
  html, body { width: 1200px; height: 712px; overflow: hidden; background: var(--page); }
  body { position: relative; font-family: "Asap Condensed", "Arial Narrow", sans-serif; color: var(--green-text); }

  .brochure {
    position: absolute; left: 85px; top: 65px; width: 1039px; height: 585px;
    background: #f3f3f1; box-shadow: 0 8px 22px rgba(0,0,0,.18);
  }
  .fold { position: absolute; top: 40px; height: 640px; border-left: 1px dashed var(--fold); }

  .photo { position: absolute; top: 65px; height: 176px; }
  .photo-massage { left: 85px; width: 258px; background: linear-gradient(160deg, #f0d7c4, #d9b49a 60%, #efe3d6); }
  .photo-facial { left: 343px; width: 260px; background: linear-gradient(170deg, #e6c3a8, #f4ece6 55%, #d8b9a2); }
  .photo-relax { left: 603px; width: 263px; background: linear-gradient(180deg, #f6eef0, #e5c8bf 60%, #c9a79d); }
  .photo-hair { left: 930px; top: 70px; width: 160px; height: 170px; background: radial-gradient(ellipse at 50% 45%, #f0dcc0, #e7cfa7 55%, #fbf7f1 78%); }

  .brand-name {
    position: absolute; left: 175px; top: 203px; font-size: 22px; font-weight: 500;
    color: var(--green-text); display: flex; align-items: center; gap: 6px;
  }
  .brand-name .dot { width: 9px; height: 9px; border-radius: 50%; background: var(--green-text); }

  .card { position: absolute; top: 241px; height: 404px; border-radius: 0 0 9px 9px; }
  .card-white-left { left: 85px; width: 253px; background: var(--white); }
  .card-olive { left: 350px; width: 508px; background: var(--olive-panel); border-radius: 0 0 12px 12px; }
  .card-white-right { left: 870px; width: 248px; background: var(--white); }

  .col { position: absolute; font-size: 8.6px; line-height: 1.2; }
  .col-massage { left: 94px; top: 245px; width: 238px; }
  .col-body { left: 354px; top: 245px; width: 246px; }
  .col-peels { left: 604px; top: 245px; width: 250px; }
  .col-hair { left: 882px; top: 240px; width: 232px; }

  .item { margin-bottom: 8px; }
  .item-title { font-size: 7.6px; text-transform: uppercase; color: var(--tan-head); font-weight: 600; margin-bottom: 1px; }
  .on-olive .item-title { color: var(--white); }
  .price { font-size: 6.4px; padding-left: 12px; margin-top: 2px; }
  .section-title { font-size: 15.5px; font-weight: 500; text-transform: uppercase; color: var(--white); margin: 0 0 1px; line-height: 1.1; }
  .col-hair .section-title { color: var(--tan-head); margin: 6px 0 3px; }
  .label { font-size: 7.4px; margin-top: 4px; }
  .line { font-size: 6.4px; padding-left: 12px; margin-top: 2px; }
  .split { display: flex; gap: 40px; }
</style>
</head>
<body>
  <div class="brochure"></div>

  <div class="photo photo-massage" role="img" aria-label="Photo of a woman receiving a back massage"></div>
  <div class="photo photo-facial" role="img" aria-label="Photo of a woman receiving a facial mask treatment"></div>
  <div class="photo photo-relax" role="img" aria-label="Photo of a smiling woman relaxing with spa candles and orchids"></div>
  <div class="photo photo-hair" role="img" aria-label="Photo of a woman with long curled blonde hair"></div>

  <div class="brand-name"><span class="dot"></span>Lumen massage</div>

  <div class="card card-white-left"></div>
  <div class="card card-olive"></div>
  <div class="card card-white-right"></div>

  <section class="col col-massage">
    <div class="item"><div class="item-title">Swedish Massage</div>Reduces and relieves stress and muscle tension. Induces deep relaxation<br>and improves circulation and range of motion.
      <div class="price">Target Area (approx 25 min.) $50 | Full Body (approx 50 min.) $70 | Extended Full Body (approx. 80 min.) $120</div></div>
    <div class="item"><div class="item-title">Prenatal Massage</div>Relieves stress on weight bearing joints and induces deep relaxation.<br>Always consult your OB/GYN.
      <div class="price">Target Areas $50 | Full Body $70</div></div>
    <div class="item"><div class="item-title">Seated Massage</div>The perfect solution for neck and shoulder pain. An abbreviated massage targeted to pressure points of the scalp, neck and shoulders.
      <div class="price">$25</div></div>
    <div class="item"><div class="item-title">Four Handed Massage... (our signature treatment)</div>The ultimate relaxation experience. Have two of our skilled therapists work on you simultaneously.
      <div class="price">target (approx. 30 min.) $100 | full body (approx. 60 min.) $140</div></div>
    <div class="item"><div class="item-title">Hot Stone Massage</div>This therapeutic treatment incorporates hot stones with classic massage movements.
      <div class="price">$85 (approx. 60 min.)</div></div>
    <div class="item"><div class="item-title">Deep Tissue Massage</div>Goes beyond Swedish Relaxation Massage by going deeper into the tissue or muscles that are responsible for holding chronic pain patterns.
      <div class="price">$90 (approx. 60 min.)</div></div>
    <div class="item"><div class="item-title">Scalp Massage</div><div class="price">(15 min.) $20</div></div>
    <div class="item"><div class="item-title">Foot Massage</div><div class="price">(15 min.) $20</div></div>
  </section>

  <section class="col col-body on-olive">
    <h2 class="section-title">Body Treatments</h2>
    <div class="item"><div class="item-title">Body Scrubs and Wraps</div>We offer a full line of customized body scrubs and wraps. These treatments help to exfoliate, remineralize, rehydrate and detoxify.<br>After a consultation with your trained therapist it will be determined which treatment will best suit your needs.
      <div class="price">Scrubs $50 and up | Wraps $50 and up | Scrub &amp; Wrap $100 and up</div></div>
    <div class="item"><div class="item-title">Backtreatment</div>This treatment is like a facial for your back. It will help refine the texture and improve the appearance of the skin on the back. This is a must for anyone wearing a backless dress.
      <div class="price">$55</div></div>
    <div class="item"><div class="item-title">Sinustreatment</div>This treatment involves steam and localized massage to give you relief from sinus pressure and help encourage the sinuses to drain.
      <div class="price">$50</div></div>
    <h2 class="section-title">Facials</h2>
    <div class="item"><div class="item-title">Express Facial</div>This facial includes cleansing, steaming, exfoliation, pressure point massage and a 5 minute maintenance treatment mask.
      <div class="price">$50</div></div>
    <div class="item"><div class="item-title">Teen Facial</div>This is an express facial with a very thorough skin care consultation to address the challenges faced by the teen years.
      <div class="price">$55</div></div>
    <div class="item"><div class="item-title">Customized Facial</div>This facial is customized to meet any skin care needs you may have. Includes cleansing, steaming, exfoliation on the décolleté, neck and shoulder. Includes a detox massage, pressure point massage and relaxation massage,<br>a 10-15 minute treatment mask, hand, arm, foot and leg massage.
      <div class="price">Women $70 | Men with shave consultation $70 | Extractions $10</div></div>
  </section>

  <section class="col col-peels on-olive">
    <div class="item"><div class="item-title">Natural Facial Peels</div>Peels are a much deeper form of exfoliation. They go one step beyond a customized facial without the redness and dehydration of some other peeling treatments. These peels are done in conjunction with a Customized Facial.
      <div class="price" style="font-size:8px">(approx. 80 min.) Royal Peel $110 | Algae Peel $95</div></div>
    <div class="item"><div class="item-title">Pumpkin Facial</div>Granuals and enzymes that encourage the removal of skin cell build up without stress or irritation of the skin.
      <div class="price" style="font-size:8px">$85</div></div>
    <div class="item"><div class="item-title">Luma Therapeutics Facial</div>Incorporating retinols, glycolics and lactic acids to improve skin tone and texture.
      <div class="price" style="font-size:8px">$75</div></div>
    <div class="item"><div class="item-title">Skin Brightening Facial</div>Helps to improve dull or uneven skin tone, sun and environmentally damaged, mature and hyperpigmented skin.
      <div class="price" style="font-size:8px">$85</div></div>
    <div class="item"><div class="item-title">Microdermabrasion</div>Renew and revitalize your skin with this non-invasive exfoliating procedure. This type of skin resurfacing can be performed in an individual session, yet provides optimum results when performed in a series.
      <div class="price" style="font-size:8px">Call for pricing</div></div>
    <div class="item"><div class="item-title">Chemical Exfoliation / Peels</div>Chemical exfoliation can help improve many skin conditions, from acne and hyperpigmentation to dull sun damaged aging skin. Enzyme, Lactic, Salicylic, Glycolic 30% &amp; 60%, Modified Jessner &amp; TCA.
      <div class="price">$85 – $150 (Series pricing available)</div>Must have consultation before booking peel. <span style="font-size:6.4px">(15 min.) NO CHARGE</span></div>
    <div class="item"><div class="item-title">Hot Stone Facial</div>Enjoy the benefits of the Customized Facial enhanced by the use of hot<br>and cold stones used during the massage.
      <div class="price" style="font-size:8px">$85</div></div>
  </section>

  <section class="col col-hair">
    <h2 class="section-title">Body Waxing</h2>
    <div class="label">full body waxing<br>(For all waxing services you must have 2-3 weeks growth.)</div>
    <div class="line">Lip/Brow/Chin/Sideburns/Stomach $15 each area and up</div>
    <div class="line">Bikini/Under Arms/Forearms start at $25 each service</div>
    <div class="line">Full Legs/Men's Back/Men's Chest $50 each service</div>
    <div class="line">Half Legs/Full Arms $30 each service</div>
    <div class="line">Brazilian Wax $75 and up</div>

    <h2 class="section-title" style="margin-top:14px">Hair</h2>
    <div class="line">All services are a la carte.</div>
    <div class="label">cuts</div>
    <div class="line">Women $24 and up | Men $21 and up | Student $21 and up</div>
    <div class="line">Child (0-11) $15 and up | Bang Trim $15 and up</div>
    <div class="label">style</div>
    <div class="line">Formal $45 and up | Bride $55 and up | Casual $18 and up</div>
    <div class="label">foil</div>
    <div class="line">Full $55 and up | Half $45 and up | Face $35 and up</div>
    <div class="label">color</div>
    <div class="line">All Over Color $40 and up</div>
    <div class="label split"><span>perm</span><span style="margin-left:60px">relaxers</span></div>
    <div class="line split"><span>Regular $65 and up</span><span>Regular $75 and up</span></div>

    <h2 class="section-title" style="margin-top:14px">Hair Extensions</h2>
    <div class="label">human hair extensions</div>
    <div style="font-size:8.6px">We offer natural human hair extensions that last 3-6 months. They attach to small strands of your own hair. Whether you just want to add length, thickness or highlights we have the solution. All our extension specialists have gone through extensive training and are certified by the manufacturer.</div>
    <div class="label" style="margin-top:8px">hair pieces</div>
  </section>

  <div class="fold" style="left:343px"></div>
  <div class="fold" style="left:866px"></div>
</body>
</html>
```